Business Card for Pottery and Jewellery Designer

A new business card design is needed to accompany a newly launching pottery and jewellery website. The company logo has been attached for use. The company is called Glazewick Studio. For a sense of the vibe please see the website (it is currently under construction but this way you'll get a feel for the style) www.GlazewickStudio.com

The website font is Pontano Sans for the body of the text with Overlock for headers.

The overall look should be clean and elegant. The back side can have just the logo. The front side should have a smaller logo and the following details displayed:

Glazewick Studio
Designer: Hollis Marrow
Phone: xxx.xxx.xxxx
Email: Designer@GlazewickStudio.com

The structure of displaying this is completely up to you. Different layouts and creative methods of displaying contact info are welcome as long as it stays clean/uncluttered.

No product photographs are to be included in the design as the catalogue changes quickly.

Colour preferences lean towards elegant and understated (charcoal grey, dark navy blue etc.)

Please let me know if you have any further questions or further details required.

Target Market(s)

Target market is 30+ year old women

Industry/Entity Type

Construction

Colors
ffffff
1b1b1b
474747
d9d9d9
fafafa
0355a3

Requirements
Must have
• The submissions so far have looked very typical and don't stand out right now. They're also all in navy with very little variation. I'm looking for something that stands out a it more while still being clean-looking.
Nice to have
• I've attached a few design samples and an idea for a backdrop. It would be great to see some designs in black, white, and grey with only a hint of color.
Should not have
• Product Images

```html
<!DOCTYPE html>
<html lang="en">
<head>
<meta charset="utf-8">
<title>Glazewick Studio — Business Card</title>
<link rel="stylesheet" href="https://fonts.googleapis.com/css2?family=Overlock:wght@400;700&family=Pontano+Sans&display=swap">
<style>
  :root {
    --white: #ffffff;
    --ink: #1b1b1b;
    --charcoal: #474747;
    --rule: #d9d9d9;
    --paper: #fafafa;
    --stage: #e9e7e4;
    --faint: #e2e2e2;
  }
  * { margin: 0; padding: 0; box-sizing: border-box; }
  html, body { width: 1200px; height: 1023px; overflow: hidden; }
  body {
    background: var(--stage);
    font-family: "Pontano Sans", sans-serif;
    color: var(--ink);
    position: relative;
  }
  .card {
    position: absolute;
    width: 560px;
    height: 320px;
    box-shadow: 0 6px 18px rgba(0,0,0,.18);
  }
  /* Back side */
  .card-back {
    left: 60px; top: 110px;
    background: var(--charcoal);
    display: flex; align-items: center; justify-content: center;
  }
  .back-emblem {
    width: 236px; height: 236px;
    border-radius: 50%;
    background: var(--white);
    display: flex; align-items: center; justify-content: center;
    text-align: center;
    font-size: 26px;
    letter-spacing: .5px;
    color: var(--charcoal);
  }
  /* Front side */
  .card-front {
    left: 580px; top: 600px;
    background: var(--white);
    display: flex;
    padding: 46px 40px;
  }
  .brand-column { flex: 1; }
  .brand {
    display: flex; align-items: center; gap: 8px;
    font-size: 19px; letter-spacing: .6px;
    text-transform: uppercase;
    color: var(--ink);
  }
  .brand-mark { width: 16px; height: 16px; background: var(--charcoal); }
  .tagline {
    margin-top: 22px;
    font-size: 12px; line-height: 22px;
    color: var(--faint);
  }
  .divider {
    width: 1px; background: var(--rule);
    margin: 40px 34px 10px;
  }
  .contact-column { flex: 1; padding-top: 40px; }
  .person-name {
    font-family: "Overlock", sans-serif;
    font-weight: 700; font-size: 19px;
  }
  .person-role { font-size: 13px; color: var(--charcoal); margin: 4px 0 10px; }
  .contact-line {
    display: flex; align-items: center; gap: 10px;
    font-size: 13px; color: var(--ink); margin-top: 7px;
  }
  .contact-icon { width: 15px; height: 15px; flex: none; }
</style>
</head>
<body>
  <section class="card card-back" aria-label="Card back">
    <div class="back-emblem">Glazewick<br>Studio</div>
  </section>

  <section class="card card-front" aria-label="Card front">
    <div class="brand-column">
      <div class="brand"><span class="brand-mark"></span>Glazewick Studio</div>
      <p class="tagline">Handmade pottery and jewellery<br>Thrown, glazed and kiln fired<br>Made slowly in small batches</p>
    </div>
    <div class="divider"></div>
    <div class="contact-column">
      <p class="person-name">Hollis Marrow</p>
      <p class="person-role">Designer</p>
      <p class="contact-line">
        <svg class="contact-icon" viewBox="0 0 16 16"><circle cx="8" cy="8" r="8" fill="#1b1b1b"/><path d="M5.2 4.2l1.6 0 .6 2-1 .8c.5 1 1.3 1.8 2.3 2.3l.8-1 2 .6v1.6c0 .4-.4.8-.8.8C7.3 11.2 4.8 8.7 4.4 5c0-.4.4-.8.8-.8z" fill="#fff"/></svg>
        xxx.xxx.xxxx
      </p>
      <p class="contact-line">
        <svg class="contact-icon" viewBox="0 0 16 16"><circle cx="8" cy="8" r="8" fill="#1b1b1b"/><rect x="3.8" y="5" width="8.4" height="6" fill="none" stroke="#fff" stroke-width="1"/><path d="M3.8 5l4.2 3.3L12.2 5" fill="none" stroke="#fff" stroke-width="1"/></svg>
        Designer@GlazewickStudio.com
      </p>
    </div>
  </section>
</body>
</html>
```